LEAFNOOK needs a flyer design!

I would like to design a flyer for my small company "LEAFNOOK". We sell stylish and innovative solutions regarding insidegardening in our webshop. We sell modern flowerpots and "green" gifts that you cannot buy in the DIY. Everyone who wants exclusive green design has to buy on our shop. Now we are planning to launch a summer sale flyer in a DIN A5 postcard. In the front we would like to generate attention and state our web-site adress. In the rear of the card we would like to give four to six examples of our products together with the respective discount of 20 to 30%. Our goal is to increase traffic on our website. Please use some of these photos of some of my products if it is useful. I also added my logo "leafnook" and the two logos of my main suppliers "wrenlo" and "claytuftz" that i would like to have named.

Target Market(s)

Hausewives, modern homeowners, restaurants

Industry/Entity Type

It Company

Font styles to use
Sans Serif

Colors

Designer to choose colors to be used in the design.

Requirements
Must have
• Finally i need a text in german language. But we can replace the english text at the end of our project.

```html
<!DOCTYPE html>
<html lang="en">
<head>
<meta charset="utf-8">
<title>LEAFNOOK – Summer Sale Flyer</title>
<link rel="stylesheet" href="https://fonts.googleapis.com/css2?family=Open+Sans:wght@400;600;700&display=swap">
<style>
  :root {
    --frame: #3b3b3b;
    --band: #3a3a3a;
    --green: #6aa332;
    --ink: #333333;
    --white: #ffffff;
    --paper: #f3f8fa;
    --sky: #cfe5ef;
  }
  * { margin: 0; padding: 0; box-sizing: border-box; }
  html, body { width: 1200px; height: 824px; overflow: hidden; background: var(--frame); }
  body { font-family: "Open Sans", sans-serif; position: relative; }

  .panel {
    position: absolute; top: 0; width: 588px; height: 824px; overflow: hidden;
    background: radial-gradient(ellipse at 50% 50%, var(--paper) 55%, var(--sky) 100%);
  }
  .panel--front { left: 0; }
  .panel--back { left: 612px; }

  /* front */
  .front-art { position: absolute; inset: 0; }
  .url-band {
    position: absolute; left: 0; top: 28px; width: 588px; height: 32px;
    background: var(--band); color: var(--white);
    font-weight: 600; font-size: 22px; line-height: 32px; text-align: center; letter-spacing: 0.5px;
  }
  .brand {
    position: absolute; left: 264px; top: 128px;
    display: flex; align-items: center; gap: 8px;
    color: var(--green); font-size: 31px; font-weight: 400; letter-spacing: 0.5px;
  }
  .brand__mark { width: 22px; height: 22px; background: var(--green); border-radius: 3px; }

  .benefits { position: absolute; left: 58px; top: 420px; list-style: none; }
  .benefits li {
    position: relative; padding-left: 46px; color: var(--white);
    font-size: 23px; line-height: 24px; letter-spacing: 0.6px; margin-bottom: 24px; width: 470px;
  }
  .benefits li svg { position: absolute; left: 0; top: 4px; }

  .sponsors { position: absolute; left: 0; top: 688px; width: 588px; text-align: center; }
  .sponsors__title { font-size: 25px; font-weight: 700; color: #222; letter-spacing: 0.5px; }
  .sponsors__list { display: flex; justify-content: center; align-items: center; gap: 34px; margin-top: 10px; }
  .sponsor { display: flex; align-items: center; gap: 8px; font-size: 36px; font-weight: 600; color: #222; }
  .sponsor--claytuftz { font-size: 24px; }
  .sponsor__square { width: 22px; height: 22px; background: var(--green); }

  /* back */
  .hero-photo { position: absolute; left: 0; top: 0; width: 256px; height: 226px; }
  .hero-badge { position: absolute; left: 220px; top: 196px; width: 24px; height: 18px; background: #1e1e1e; border: 2px solid #eee; }
  .headline { position: absolute; left: 276px; top: 56px; }
  .headline__d { position: absolute; left: 0; top: -6px; font-size: 106px; font-weight: 600; color: var(--green); line-height: 1; }
  .headline__pct { position: absolute; left: 76px; top: 4px; font-size: 37px; color: var(--ink); white-space: nowrap; line-height: 1; }
  .headline__word { position: absolute; left: 70px; top: 50px; font-size: 45px; color: var(--ink); white-space: nowrap; line-height: 1; letter-spacing: 1.5px; }
  .headline__tag { position: absolute; left: 4px; top: 106px; font-size: 23px; font-weight: 600; color: var(--green); white-space: nowrap; letter-spacing: 0.5px; }

  .products {
    position: absolute; left: 67px; top: 246px; width: 450px; height: 498px;
    background: var(--white);
    display: grid; grid-template-columns: 198px 252px; grid-template-rows: 196px 141px 161px;
  }
  .product { position: relative; }
  .product__image { position: absolute; left: 0; top: 0; right: 0; bottom: 20px; }
  .product--right .product__image { left: 2px; }
  .product__name {
    position: absolute; left: 0; right: 0; bottom: 0; height: 20px;
    background: var(--band); color: var(--white);
    font-size: 14px; font-weight: 600; line-height: 20px; text-align: center; letter-spacing: 0.4px;
  }
  .product--right .product__name { left: 2px; }
  .badge { position: absolute; right: 6px; top: 8px; width: 24px; height: 16px; background: #1e1e1e; border: 2px solid #fff; }

  .contact {
    position: absolute; left: 67px; top: 759px; width: 450px; height: 36px;
    background: var(--green); color: var(--white);
    font-size: 16.5px; line-height: 36px; text-align: center; letter-spacing: 0.5px;
  }
</style>
</head>
<body>

<section class="panel panel--front">
  <svg class="front-art" width="588" height="824" viewBox="0 0 588 824">
    <defs>
      <linearGradient id="greenWave" x1="0" y1="0" x2="0" y2="1">
        <stop offset="0" stop-color="#c3da86"/>
        <stop offset="0.45" stop-color="#93bb52"/>
        <stop offset="1" stop-color="#5f9329"/>
      </linearGradient>
      <linearGradient id="lounge" x1="0" y1="0" x2="0" y2="1">
        <stop offset="0" stop-color="#8a8f94"/>
        <stop offset="0.45" stop-color="#3f5b86"/>
        <stop offset="1" stop-color="#6b4a32"/>
      </linearGradient>
      <linearGradient id="moss" x1="0" y1="0" x2="0" y2="1">
        <stop offset="0" stop-color="#6a6660"/>
        <stop offset="0.4" stop-color="#8a7a62"/>
        <stop offset="0.6" stop-color="#5a9a3a"/>
        <stop offset="1" stop-color="#2a2a2a"/>
      </linearGradient>
      <linearGradient id="blooms" x1="0" y1="0" x2="0" y2="1">
        <stop offset="0" stop-color="#4d4a44"/>
        <stop offset="0.4" stop-color="#c9c3d6"/>
        <stop offset="1" stop-color="#e9e9e6"/>
      </linearGradient>
      <radialGradient id="branch" cx="0.5" cy="0.5" r="0.5">
        <stop offset="0" stop-color="#b08a5a" stop-opacity="0.55"/>
        <stop offset="0.6" stop-color="#d6a3b8" stop-opacity="0.3"/>
        <stop offset="1" stop-color="#d6a3b8" stop-opacity="0"/>
      </radialGradient>
    </defs>
    <ellipse role="img" aria-label="Illustrated blossoming branches" cx="120" cy="100" rx="150" ry="80" fill="url(#branch)"/>
    <ellipse role="img" aria-label="Illustrated blossoming branch" cx="40" cy="680" rx="90" ry="60" fill="url(#branch)"/>
    <rect x="0" y="170" width="588" height="200" fill="#ffffff"/>
    <rect role="img" aria-label="Photo of a lounge with white vases of pink flowers on a wooden table" x="0" y="174" width="214" height="190" fill="url(#lounge)"/>
    <rect role="img" aria-label="Photo of a black bowl planter filled with moss" x="221" y="174" width="205" height="190" fill="url(#moss)"/>
    <rect role="img" aria-label="Photo of a white planter with white and purple flowers" x="432" y="174" width="156" height="190" fill="url(#blooms)"/>
    <path d="M0,342 C170,318 380,262 588,276 L588,600 L0,600 Z" fill="#ffffff"/>
    <path d="M0,362 C170,336 380,286 588,296 L588,632 C400,662 180,668 0,648 Z" fill="url(#greenWave)"/>
  </svg>

  <div class="url-band">www.leafnook.de</div>

  <div class="brand"><span>LEAFNOOK</span><span class="brand__mark"></span></div>

  <ul class="benefits">
    <li><svg width="30" height="24" viewBox="0 0 30 24"><path d="M2,13 L11,21 L28,3" fill="none" stroke="#fff" stroke-width="5" stroke-linecap="round" stroke-linejoin="round"/></svg>stylish and innovative solutions<br>for your garden</li>
    <li><svg width="30" height="24" viewBox="0 0 30 24"><path d="M2,13 L11,21 L28,3" fill="none" stroke="#fff" stroke-width="5" stroke-linecap="round" stroke-linejoin="round"/></svg>modern flowerpots and "green"<br>gifts</li>
    <li><svg width="30" height="24" viewBox="0 0 30 24"><path d="M2,13 L11,21 L28,3" fill="none" stroke="#fff" stroke-width="5" stroke-linecap="round" stroke-linejoin="round"/></svg>discounts of 20 to 30%</li>
  </ul>

  <div class="sponsors">
    <p class="sponsors__title">sponsored by</p>
    <div class="sponsors__list">
      <span class="sponsor">wrenlo</span>
      <span class="sponsor sponsor--claytuftz"><span class="sponsor__square"></span>claytuftz</span>
    </div>
  </div>
</section>

<section class="panel panel--back">
  <div class="hero-photo" role="img" aria-label="Photo of pink and purple orchids in white square pots on a dark side table" style="background: linear-gradient(180deg, #e6e6e6 0%, #b9b9b9 30%, #c85aa0 45%, #efefef 58%, #2a2a2a 66%, #1b1b1b 100%);"></div>
  <span class="hero-badge"></span>

  <div class="headline">
    <span class="headline__d">D</span>
    <span class="headline__pct">20 to 30%</span>
    <span class="headline__word">ISCOUNT</span>
    <span class="headline__tag">don’t miss it!</span>
  </div>

  <div class="products">
    <div class="product">
      <div class="product__image" role="img" aria-label="Tall square light grey planters" style="background: linear-gradient(90deg, #f4f4f2 0%, #d3d2cd 30%, #c2c1bb 70%, #f4f4f2 100%);"></div>
      <div class="product__name">product name</div>
    </div>
    <div class="product product--right">
      <div class="product__image" role="img" aria-label="Upside-down hanging white planters with green plants" style="background: linear-gradient(180deg, #ffffff 0%, #eef1ec 35%, #7fa565 65%, #e9efe3 100%);"></div>
      <div class="product__name">product name</div>
    </div>
    <div class="product">
      <div class="product__image" role="img" aria-label="Low wide dark grey bowl planter" style="background: linear-gradient(180deg, #ffffff 0%, #f2f2f2 25%, #6b6b6b 45%, #555555 72%, #ffffff 90%);"></div>
      <div class="product__name">product name</div>
    </div>
    <div class="product product--right">
      <div class="product__image" role="img" aria-label="Colourful hanging pots with trailing plants against a white wall" style="background: linear-gradient(180deg, #f0f0ee 0%, #8fc7b2 28%, #6f9a4c 58%, #b9a27a 80%, #ecebe8 100%);"></div>
      <div class="product__name">product name</div>
    </div>
    <div class="product">
      <div class="product__image" role="img" aria-label="Two round grey bowl planters" style="background: linear-gradient(180deg, #ffffff 0%, #ffffff 22%, #7d7d7d 40%, #5f5f5f 80%, #ffffff 95%);"></div>
      <span class="badge"></span>
      <div class="product__name">product name</div>
    </div>
    <div class="product product--right">
      <div class="product__image" role="img" aria-label="Long white tray planter with silvery air plants" style="background: linear-gradient(180deg, #242424 0%, #5a5a5a 30%, #dedbd2 50%, #f7f7f5 72%, #b8b4ac 100%);"></div>
      <div class="product__name">product name</div>
    </div>
  </div>

  <div class="contact">Tel: 04713 - 286154 &nbsp;|&nbsp; E-Mail: info@leafnook.de</div>
</section>

</body>
</html>
```